Redesign of existing website for a corporate advisory business focussed on technology

We need a redesign of our website. We are a corporate advisory business based in Sydney. Our focus is on the technology and life-science sectors. We assist our clients with capital raisings, mergers and acquisitions and other corporate transactions.

Our business is called "Harbour Ridge Partners"
Our current website is www.harbourridgeadv.com.au

I'd like to see a complete re-design of the site. (I'm happy to keep any of the existing images - but equally happy to scrap them completely and "start again".)

My preference is that the logo remain as it is. However, I would be very open to a re-colouring of the logo if it works better with a new webiste design.

The content of the website will remain the same. I'd like one additional section - "News" - which will allow us to manually post news items and which will pull in news feeds from current and past clients.

In terms of positioning / look-and-feel:

Our clients fall into two categories. I'd like the website to appeal to both:

1. The first category is: Executives from established technology or life-science companies (private or public), who engage us to assist with strategy, capital raising, corporate transactions.

2. The second category is: Entrepreneurs looking for advice in accessing angel funding or venture capital. The site should appeal to young tech-savvy entrepreneurs who are looking to engage a firm to provide such assistance.

To accomodate both target groups, the overriding feel should be one of professionalism, stability, trust and expertise. However, while the site should look fairly "corporate", I'd like it to feel contemporary and have an element of creativity and flair, reflecting the fact that our clients are often early-stage, innovative, technology companies. (I know this might be a tricky balance...)

Target Market(s)

Potential clients. Typically executives at technology or life-science companies or (more typically) entrepreneurs building their own companies

Industry/Entity Type

Business

Requirements
Must have
• 1. All content on the existing website
2. An additional section called "News" that allows us to easily add news items or articles and ideally which accepts news feeds from a handful of past and present clients
3. An ability to easily update and edit content
Should not have
• The site should not have "gimmicks". (Definitely no devices like the moving arrow in the current site!)

It should be fairly conservative, while still feeling contemporary and fresh.

```html
<!DOCTYPE html>
<html lang="en">
<head>
<meta charset="utf-8">
<title>Harbour Ridge Partners</title>
<link rel="stylesheet" href="https://fonts.googleapis.com/css2?family=Oswald:wght@300;400&family=PT+Sans+Narrow:wght@400;700&family=PT+Sans:wght@400&display=swap">
<style>
  :root {
    --orange: #e8772e;
    --orange-light: #f28c48;
    --orange-dark: #dc6a20;
    --tab-active: #d95a0d;
    --rust: #c8601a;
    --brown: #6b2f14;
    --footer: #5c2810;
    --grey-band: #eceeef;
    --ink: #3a3a3a;
    --text: #333;
    --white: #fff;
  }
  * { box-sizing: border-box; margin: 0; padding: 0; }
  html, body { width: 733px; height: 1200px; overflow: hidden; background: var(--white); }
  body { position: relative; font-family: "PT Sans", sans-serif; color: var(--text); }
  .abs { position: absolute; }

  /* header */
  .brand { left: 28px; top: 21px; display: flex; align-items: center; gap: 12px; }
  .brand-dot { width: 50px; height: 50px; border-radius: 50%; background: var(--orange); }
  .brand-name { font-size: 18px; color: var(--ink); letter-spacing: .1px; }
  .main-nav { left: 300px; top: 12px; width: 397px; height: 80px;
    background: linear-gradient(var(--orange-light), var(--orange-dark)); }
  .main-nav a { position: absolute; top: 0; height: 80px; display: flex; align-items: center; justify-content: center;
    color: var(--white); text-decoration: none; font-family: "PT Sans Narrow", sans-serif; font-size: 11px; }
  .main-nav a.is-active { background: var(--tab-active); height: 96px; padding-bottom: 16px; }
  .nav-sep { position: absolute; top: 0; width: 1px; height: 80px; background: rgba(120,40,0,.25); }

  /* hero */
  .hero { left: 25px; top: 93px; width: 672px; height: 384px; background: var(--grey-band); }
  .hero-slide { left: 23px; top: 28px; width: 625px; height: 308px;
    background:
      linear-gradient(180deg, rgba(0,0,0,0) 50%, rgba(70,58,52,.45) 100%),
      linear-gradient(90deg, #f1f1f1 0%, #e6e6e6 55%, #d9d9d9 56%, #e4e4e4 100%);
    box-shadow: 0 4px 6px rgba(0,0,0,.3); }
  .hero-title { left: 31px; top: 15px; width: 500px; font-family: "Oswald", sans-serif; font-weight: 300;
    font-size: 21.5px; line-height: 31px; color: #3a3a3a; text-transform: uppercase; }
  .slider-dots { left: 321px; top: 351px; display: flex; gap: 5px; }
  .slider-dots span { width: 14px; height: 14px; border-radius: 50%; background: #555; }

  /* features */
  .features { left: 25px; top: 477px; width: 672px; height: 355px;
    background: linear-gradient(var(--orange-light), var(--orange-dark)); color: var(--white); }
  .feature-title { font-family: "PT Sans Narrow", sans-serif; font-weight: 700; font-size: 27px; top: 38px; }
  .feature-photo { top: 93px; width: 200px; height: 106px; border: 6px solid var(--brown); }
  .feature-text { top: 212px; width: 185px; font-size: 9.3px; line-height: 12.5px; }
  .ticks { list-style: none; }
  .ticks li { display: flex; align-items: center; gap: 7px; height: 20.3px; font-size: 9.5px; white-space: nowrap; }
  .ticks svg { flex: none; }
  .btn-more { top: 295px; width: 52px; height: 30px; background: linear-gradient(#f4f4f4, #d6d6d6);
    box-shadow: 0 2px 3px rgba(0,0,0,.3); color: #555; font-size: 9.5px;
    display: flex; align-items: center; justify-content: center; }

  /* lower */
  .section-title { font-family: "PT Sans Narrow", sans-serif; font-weight: 700; font-size: 27px;
    color: var(--rust); top: 861px; }
  .lead-photo { left: 48px; top: 915px; width: 166px; height: 185px; border: 6px solid var(--orange);
    background:
      linear-gradient(180deg, rgba(0,0,0,0) 45%, rgba(60,48,40,.55) 100%),
      linear-gradient(90deg, #e4e8ea 0%, #cfd5d8 50%, #a99880 100%); }
  .lead-intro { left: 227px; top: 917px; width: 206px; font-size: 9.3px; line-height: 13px;
    color: var(--orange); text-align: justify; }
  .lead-ticks { left: 227px; top: 951px; color: #333; }
  .lead-ticks li { gap: 10px; }
  .lead-body { left: 231px; top: 1024px; width: 205px; font-size: 9px; line-height: 12.5px; color: #333; }
  .btn-solid { left: 397px; top: 1070px; width: 52px; height: 30px; background: #b54a10; color: var(--white);
    font-size: 9.5px; display: flex; align-items: center; justify-content: center; }
  .news-nav { left: 629px; top: 866px; width: 45px; height: 21px; border-radius: 3px;
    background: linear-gradient(#c45a1a, #9b3f0c); }
  .news-photo { left: 475px; top: 914px; width: 200px; height: 102px; border: 5px solid #e6e6e6;
    background:
      linear-gradient(180deg, rgba(0,0,0,0) 40%, rgba(30,30,30,.45) 100%),
      linear-gradient(90deg, #8e8e8e 0%, #d6d6d6 45%, #b4b4b4 70%, #5a5a5a 100%); }
  .news-icon { left: 476px; top: 1036px; }
  .news-date { left: 499px; top: 1030px; font-size: 12px; color: #777; }
  .news-head { left: 496px; top: 1044px; font-size: 9.5px; color: var(--orange); }
  .news-body { left: 487px; top: 1067px; width: 190px; font-size: 9px; line-height: 13px; color: #333; }

  .site-footer { left: 0; top: 1133px; width: 733px; height: 67px; background: var(--footer); }
  .copyright { left: 49px; top: 21px; font-size: 7.5px; color: var(--white); }
</style>
</head>
<body>
  <header>
    <div class="abs brand"><span class="brand-dot"></span><span class="brand-name">harbour ridge partners</span></div>
    <nav class="abs main-nav">
      <a href="#" class="is-active" style="left:40px;width:54px">HOME</a>
      <a href="#" style="left:94px;width:68px">ABOUT US</a>
      <span class="nav-sep" style="left:162px"></span>
      <a href="#" style="left:162px;width:65px">SERVICE</a>
      <span class="nav-sep" style="left:227px"></span>
      <a href="#" style="left:227px;width:71px">PROJECTS</a>
      <span class="nav-sep" style="left:298px"></span>
      <a href="#" style="left:298px;width:65px">CONTACT</a>
    </nav>
  </header>

  <section class="abs hero">
    <div class="abs hero-slide" role="img" aria-label="Photo of four business colleagues in a bright office">
      <h1 class="abs hero-title">Lorem ipsum is simply dummy text of the printing and typesetting industry....</h1>
    </div>
    <div class="abs slider-dots"><span></span><span></span><span></span></div>
  </section>

  <section class="abs features">
    <h2 class="abs feature-title" style="left:28px">MOTIVATE</h2>
    <h2 class="abs feature-title" style="left:249px">VISION</h2>
    <h2 class="abs feature-title" style="left:474px">WIN</h2>

    <div class="abs feature-photo" role="img" aria-label="Photo of colleagues working at a laptop" style="left:23px;background:linear-gradient(90deg,#e6e6e6 0%,#3a3a3a 35%,#cfcfcf 55%,#2e2e2e 100%)"></div>
    <div class="abs feature-photo" role="img" aria-label="Photo of business people shaking hands" style="left:236px;background:linear-gradient(90deg,#2c3446 0%,#e9ecf2 45%,#c9d2e0 65%,#27304a 100%)"></div>
    <div class="abs feature-photo" role="img" aria-label="Photo of a business team standing together" style="left:449px;background:linear-gradient(180deg,#c9ced6 0%,#e7dccf 60%,#8b8078 100%)"></div>

    <p class="abs feature-text" style="left:36px">Nulla venenatis. In pede mi, aliquet sit amet, euismod in, autor ut, ligula. Lorem ipsum dolor sit amet, consectetuer elit. praesent vestibulum molestie lacus.</p>
    <ul class="abs ticks" style="left:246px;top:217px">
      <li><svg width="14" height="12" viewBox="0 0 14 12"><path d="M1 6l4 4 8-9" fill="none" stroke="#fff" stroke-width="2.5"/></svg>Lorem ipsum dolor sit amet</li>
      <li><svg width="14" height="12" viewBox="0 0 14 12"><path d="M1 6l4 4 8-9" fill="none" stroke="#fff" stroke-width="2.5"/></svg>Consector adipiscing elit.</li>
      <li><svg width="14" height="12" viewBox="0 0 14 12"><path d="M1 6l4 4 8-9" fill="none" stroke="#fff" stroke-width="2.5"/></svg>Praesent vestibulam molestie lacus</li>
      <li><svg width="14" height="12" viewBox="0 0 14 12"><path d="M1 6l4 4 8-9" fill="none" stroke="#fff" stroke-width="2.5"/></svg>Aenean nomutory hendicity mauris</li>
      <li><svg width="14" height="12" viewBox="0 0 14 12"><path d="M1 6l4 4 8-9" fill="none" stroke="#fff" stroke-width="2.5"/></svg>Phasellus porta suscerp various mi.</li>
    </ul>
    <p class="abs feature-text" style="left:457px;text-align:justify;width:203px">Fosce eulsmod consequence ante. Lorem ipsumdolor sit amet, consectour adipsing elit. Pellesed solor.Aliquam congue fermentum nisl. Mauris accumsan nulla vel diam.</p>

    <div class="abs btn-more" style="left:29px">more</div>
    <div class="abs btn-more" style="left:453px">more</div>
  </section>

  <h2 class="abs section-title" style="left:48px">LEAD BY EXAMPLE</h2>
  <div class="abs lead-photo" role="img" aria-label="Photo of a woman presenting to a meeting"></div>
  <p class="abs lead-intro">Fosce eulsmod consequence ante. Lorem Ipsumdolor sit amet, consectour adipsing elit.</p>
  <ul class="abs ticks lead-ticks">
    <li><svg width="14" height="12" viewBox="0 0 14 12"><path d="M1 6l4 4 8-9" fill="none" stroke="#e8772e" stroke-width="2.5"/></svg>Lorem ipsum dolor sit amet</li>
    <li><svg width="14" height="12" viewBox="0 0 14 12"><path d="M1 6l4 4 8-9" fill="none" stroke="#e8772e" stroke-width="2.5"/></svg>Consector adipiscing elit.</li>
    <li><svg width="14" height="12" viewBox="0 0 14 12"><path d="M1 6l4 4 8-9" fill="none" stroke="#e8772e" stroke-width="2.5"/></svg>Praesent vestibulam molestie lacus</li>
  </ul>
  <p class="abs lead-body">Pellentesque dolor. Aliquam congue rementum nist. Mauns accumsan nulla vel diam. Sed in la cus uteniamadipiscing aliquet. Nulla Venetis.</p>
  <div class="abs btn-solid">more</div>

  <h2 class="abs section-title" style="left:477px">NEWS</h2>
  <div class="abs news-nav">
    <svg width="45" height="21" viewBox="0 0 45 21"><path d="M16 6.5l-4 4 4 4M29 6.5l4 4-4 4" fill="none" stroke="#fff" stroke-width="1.3"/></svg>
  </div>
  <div class="abs news-photo" role="img" aria-label="Photo of colleagues reviewing work at a laptop"></div>
  <svg class="abs news-icon" width="14" height="14" viewBox="0 0 14 14"><rect x="1" y="1" width="12" height="8" fill="none" stroke="#333" stroke-width="1.5"/><path d="M5 13h4M7 9v4" stroke="#333" stroke-width="1.5"/></svg>
  <p class="abs news-date">28.04.2012</p>
  <p class="abs news-head">Fosce eulsmod consequence ante</p>
  <p class="abs news-body">Lorem ipsum dolor sit amet, consectetuer elit.praesent vestibulum molestie lacus.</p>

  <footer class="abs site-footer">
    <p class="abs copyright">Copyright@2012.All Rights Reserved</p>
  </footer>
</body>
</html>
```